Redesign start page for existing online shop

We are selling building material (chimneys and flue pipes) as well as fireplaces (stoves). For this online shop we need a new start page. The domain is brunnfeld-bauwaren.de. Here you can see the current design. We want a smoother design with just one banner in the middle instead of the three in the first row. The look has to be more professional and trustworthy. You can therefore play with the colors. We want to try some different orange instead of our yellow / orange color. A few more things: - The phone number has to be bigger and more highlighted - So the 5 advantages at the top should be shown in a different way - New design for the products below - New footer

Target Market(s)

Germany and other countries in Europe.

Industry/Entity Type

Home Builder

Number of Pages Required

1 page

Other font styles liked:
• Please se the font on our current site.

Colors
f78f20
f68d4c

Requirements
Must have
• - Clear design - Trustworthy look - All elements Which are now shown shoulderstand be still there after redesigning -
Nice to have
• - See the Following sites to have a clou about our wishes: kalvesto.de flinkrabe.de

```html
<!DOCTYPE html>
<html lang="en">
<head>
<meta charset="utf-8">
<title>Brunnfeld Bauwaren – Start page</title>
<link rel="stylesheet" href="https://fonts.googleapis.com/css2?family=Roboto:wght@300;400;500;700&display=swap">
<style>
  :root {
    --orange: #f78f20;
    --orange-deep: #f7771d;
    --ink: #2f2f2f;
    --text: #555;
    --muted: #8a8a8a;
    --faint: #c9c9c9;
    --line: #e3e3e3;
    --band: #f8f9fc;
    --tip: #fbf3da;
    --dark: #2b2b2b;
    --neutral: #e6e6e6;
    --white: #fff;
  }
  * { box-sizing: border-box; margin: 0; padding: 0; }
  html, body { width: 747px; height: 1200px; overflow: hidden; }
  body { position: relative; background: var(--white); font-family: "Roboto", Arial, sans-serif; color: var(--text); -webkit-font-smoothing: antialiased; }

  .section-title { position: absolute; left: 0; width: 747px; text-align: center; font-weight: 400; font-size: 24px; color: var(--ink); }

  /* product cards */
  .card { position: absolute; width: 277px; height: 105px; border: 1px solid var(--line); background: var(--white); }
  .card .media { position: absolute; left: 0; top: 0; width: 134px; height: 103px; border-right: 1px solid var(--line); }
  .card .media::after { content: ""; position: absolute; right: -6px; top: 44px; width: 10px; height: 10px; background: var(--white); border-top: 1px solid var(--line); border-right: 1px solid var(--line); transform: rotate(45deg); }
  .card .shot { position: absolute; left: 26px; top: 14px; width: 72px; height: 62px; border-radius: 4px; }
  .card .price { position: absolute; left: 90px; top: 71px; width: 44px; height: 25px; background: var(--orange-deep); color: var(--white); border-radius: 2px; text-align: right; padding: 3px 4px 0 0; }
  .price small { display: block; font-size: 5.5px; font-weight: 500; line-height: 7px; }
  .price b { display: block; font-size: 9px; font-weight: 700; line-height: 11px; }
  .card h3 { position: absolute; left: 150px; width: 114px; top: 12px; text-align: center; font-size: 9.5px; font-weight: 700; color: var(--ink); line-height: 11px; }
  .card p { position: absolute; left: 150px; width: 114px; top: 38px; text-align: center; font-size: 7.2px; line-height: 12px; color: var(--text); }
  .card .go { position: absolute; right: -1px; bottom: -1px; width: 17px; height: 17px; background: var(--dark); }
  .card .go svg { position: absolute; left: 5px; top: 4px; }

  .btn-more { position: absolute; left: 316px; top: 372px; width: 114px; height: 23px; border-radius: 12px; background: var(--orange-deep); color: var(--white); font-size: 8px; font-weight: 700; text-align: center; line-height: 23px; letter-spacing: .2px; }

  /* why section */
  .why-band { position: absolute; left: 0; top: 428px; width: 747px; height: 488px; background: var(--band); border-top: 1px solid #eef0f4; }
  .why-lead { position: absolute; left: 0; top: 504px; width: 747px; text-align: center; font-size: 12.5px; line-height: 14px; color: var(--ink); }
  .why-photo { position: absolute; left: 87px; top: 574px; width: 217px; height: 216px; background: linear-gradient(160deg, #4f7a3c 0%, #8a8f86 35%, #c58e2d 60%, #7d8583 100%); }
  .why-box { position: absolute; left: 333px; top: 573px; width: 327px; height: 296px; background: var(--white); border: 1px solid var(--line); }
  .why-box .copy { position: absolute; left: 20px; top: 19px; width: 292px; font-size: 6.9px; line-height: 12px; color: var(--text); }
  .why-box .copy p + p { margin-top: 12px; }
  .tip { position: absolute; left: 20px; top: 125px; width: 290px; height: 66px; background: var(--tip); border-radius: 3px; }
  .tip svg { position: absolute; left: 9px; top: 11px; }
  .tip h4 { position: absolute; left: 30px; top: 13px; font-size: 7px; font-weight: 700; color: var(--ink); }
  .tip p { position: absolute; left: 30px; top: 26px; width: 250px; font-size: 5.6px; line-height: 7px; color: var(--text); }
  .faq { position: absolute; left: 0; top: 208px; width: 325px; list-style: none; }
  .faq li { position: relative; height: 20.5px; border-top: 1px solid var(--line); padding-left: 20px; font-size: 7px; font-weight: 500; color: var(--ink); line-height: 20px; }
  .faq li svg { position: absolute; right: 10px; top: 8px; }

  /* trust */
  .seal { position: absolute; left: 87px; top: 945px; width: 62px; height: 62px; border-radius: 4px; background: var(--neutral); }
  .trust-title { position: absolute; left: 172px; top: 951px; font-size: 9.5px; font-weight: 700; color: var(--ink); }
  .trust-text { position: absolute; left: 171px; top: 969px; width: 150px; font-size: 7.2px; line-height: 12px; color: var(--text); }
  .made-mark { position: absolute; left: 364px; top: 966px; width: 113px; height: 28px; border-radius: 3px; background: var(--neutral); }
  .trust-right { position: absolute; left: 516px; top: 966px; width: 150px; font-size: 7.2px; line-height: 12px; color: var(--text); }
  .rule { position: absolute; left: 0; top: 1036px; width: 747px; height: 1px; background: #eceef2; }

  /* footer */
  .brand { position: absolute; left: 87px; top: 1074px; display: flex; align-items: center; gap: 6px; }
  .brand i { display: block; width: 26px; height: 26px; border-radius: 50%; border: 2px solid var(--orange); }
  .brand span { font-size: 12px; font-weight: 500; color: var(--ink); line-height: 13px; letter-spacing: .2px; }
  .copyright { position: absolute; left: 87px; top: 1112px; font-size: 5.6px; line-height: 8px; color: var(--faint); }
  .foot-head { position: absolute; top: 1075px; font-size: 7px; font-weight: 500; color: var(--ink); }
  .foot-links { position: absolute; top: 1092px; list-style: none; font-size: 6px; line-height: 12px; color: var(--muted); text-transform: uppercase; letter-spacing: .2px; }
  .pay { position: absolute; height: 12px; background: #d3d3d3; border-radius: 3px; }
  .pay.round { border-radius: 50%; width: 12px; }
</style>
</head>
<body>

  <h1 class="section-title" style="top:34px;">Our Products</h1>

  <article class="card" style="left:87px;top:106px;">
    <div class="media"><div class="shot" role="img" aria-label="Stainless steel chimney cover" style="background:linear-gradient(135deg,#f2f2f2,#a9abad);"></div>
      <div class="price"><small>FROM</small><b>€ 116,50</b></div></div>
    <h3>chimney cover</h3>
    <p>Fireplace covers for all chimneys purchased individually. Highest durability and quality for your chimney.</p>
    <div class="go"><svg width="7" height="9" viewBox="0 0 7 9"><path d="M1.5 1l4 3.5-4 3.5" stroke="#fff" stroke-width="1.5" fill="none"/></svg></div>
  </article>

  <article class="card" style="left:386px;top:106px;">
    <div class="media"><div class="shot" role="img" aria-label="Wall duct panels" style="background:linear-gradient(135deg,#eeeae2,#b9b8b3);"></div>
      <div class="price"><small>FROM</small><b>€ 99,90</b></div></div>
    <h3>Wanddurchführung</h3>
    <p>Wanddurchführungen für die sichere Durchführung von Abgasrohren durch Hauswände. Brandschutz auf höchstem Niveau.</p>
    <div class="go"><svg width="7" height="9" viewBox="0 0 7 9"><path d="M1.5 1l4 3.5-4 3.5" stroke="#fff" stroke-width="1.5" fill="none"/></svg></div>
  </article>

  <article class="card" style="left:87px;top:230px;">
    <div class="media"><div class="shot" role="img" aria-label="Black wood-burning stove" style="background:linear-gradient(180deg,#3a3a3a,#1f1f1f 45%,#a5521c 55%,#2a2a2a 70%);"></div>
      <div class="price"><small>FROM</small><b>€1.159,00</b></div></div>
    <h3>Kaminofen</h3>
    <p>Kaminöfen mit hervorragendem Preis- / Leistungsverhältnis versandkostenfrei online bestellen. Langlebige Qualität und Sicherheit für Ihr Haus.</p>
    <div class="go"><svg width="7" height="9" viewBox="0 0 7 9"><path d="M1.5 1l4 3.5-4 3.5" stroke="#fff" stroke-width="1.5" fill="none"/></svg></div>
  </article>

  <article class="card" style="left:386px;top:230px;">
    <div class="media"><div class="shot" role="img" aria-label="Lightweight construction chimney" style="background:linear-gradient(180deg,#8a2a1c,#b9b4ab 40%,#8d8a84);"></div>
      <div class="price"><small>FROM</small><b>€ 63,00</b></div></div>
    <h3>Lightweight<br>construction chimney</h3>
    <p style="top:40px;">Lightweight construction chimneys are the perfect solution for an interior chimney. Light elements allow for quick and easy installation.</p>
    <div class="go"><svg width="7" height="9" viewBox="0 0 7 9"><path d="M1.5 1l4 3.5-4 3.5" stroke="#fff" stroke-width="1.5" fill="none"/></svg></div>
  </article>

  <a class="btn-more">MORE PRODUCTS</a>

  <section class="why-band"></section>
  <h2 class="section-title" style="top:462px;">Why we are best</h2>
  <p class="why-lead">Stainless steel chimneys, chimney extensions, stovepipes and<br>chimney accessories - at brunnfeld-bauwaren.de buy anything</p>

  <div class="why-photo" role="img" aria-label="Roofer fastening shingles with a nail gun"></div>

  <div class="why-box">
    <div class="copy">
      <p>Can I use a steel chimney for sale on the Internet? This question you have probably never asked. For other products which is a matter of course, but with a stainless steel chimney you do not think first to the online shopping . There are the all around the subject for several years various platforms steel chimney offer.</p>
      <p>However, these providers operate their web shop only incidentally. This is reflected in the poor usability and the partly very outdated technology of pages. Brunnfeld Bauwaren has gone a new way here.</p>
    </div>
    <div class="tip">
      <svg width="14" height="18" viewBox="0 0 14 18" fill="none" stroke="#f0a23a" stroke-width="1"><path d="M7 3a4.5 4.5 0 0 0-2.6 8.2V13h5.2v-1.8A4.5 4.5 0 0 0 7 3z"/><path d="M5 15h4M5.6 16.6h2.8M7 0v1.4M1 3l1 1M13 3l-1 1M0 8h1.4M12.6 8H14"/></svg>
      <h4>Another tip:</h4>
      <p>All chimneys can be wonderfully with a stovepipe connect Veltrohr. Here there is a large Auswahl at various lengths, colors and angles. In addition, more recently, insulated stovepipes are available. This double-walled furnace tubes reduce the distance that must be maintained to combustible materials to a minimum.</p>
    </div>
    <ul class="faq">
      <li>Steel chimney, chimney kit and stainless steel chimney - all from one source.<svg width="8" height="5" viewBox="0 0 8 5"><path d="M.5.5L4 4 7.5.5" stroke="#f78f20" fill="none"/></svg></li>
      <li>uild chimney extension and cowl extension low self.<svg width="8" height="5" viewBox="0 0 8 5"><path d="M.5.5L4 4 7.5.5" stroke="#f78f20" fill="none"/></svg></li>
      <li>Chimney cap, chimney cover and Kaminabdeckplatte stainless steel to measure.<svg width="8" height="5" viewBox="0 0 8 5"><path d="M.5.5L4 4 7.5.5" stroke="#f78f20" fill="none"/></svg></li>
      <li>Chimney fans, draft stabilizer, fire doors and other specialty products<svg width="8" height="5" viewBox="0 0 8 5"><path d="M.5.5L4 4 7.5.5" stroke="#f78f20" fill="none"/></svg></li>
    </ul>
  </div>

  <div class="seal" aria-hidden="true"></div>
  <h3 class="trust-title">25-year guarantee</h3>
  <p class="trust-text">To meet our premium quality and our service pledges, please contact us, of course, 25-year guarantee on all stainless steel chimneys and steel chimney components.</p>

  <div class="made-mark" aria-hidden="true"></div>
  <p class="trust-right">We offer exclusive products of German brand manufacturers. Our full range is manufactured from industry leaders and is subject to constant quality controls. For your safety, only the best for a fair price.</p>

  <div class="rule"></div>

  <div class="brand"><i></i><span>BRUNNFELD<br>BAUWAREN</span></div>
  <p class="copyright">© 2016 BRUNNFELD-BAUWAREN.DE<br>ALL RIGHTS RESERVED.</p>

  <h4 class="foot-head" style="left:232px;">OTHER LINKS</h4>
  <ul class="foot-links" style="left:234px;">
    <li>Frequently asked questions</li><li>About us</li><li>Conditions</li><li>Revocation delivery</li><li>Data protection</li>
  </ul>
  <ul class="foot-links" style="left:359px;">
    <li>Imprint</li><li>Contact us</li><li>Blog</li><li>Glossary</li>
  </ul>

  <h4 class="foot-head" style="left:516px;">WE ACCEPT</h4>
  <div class="pay" style="left:516px;top:1104px;width:25px;"></div>
  <div class="pay" style="left:558px;top:1104px;width:24px;"></div>
  <div class="pay" style="left:597px;top:1104px;width:28px;"></div>
  <div class="pay" style="left:637px;top:1104px;width:29px;"></div>
  <div class="pay round" style="left:525px;top:1128px;"></div>
  <div class="pay" style="left:557px;top:1128px;width:28px;"></div>
  <div class="pay" style="left:597px;top:1128px;width:30px;"></div>

</body>
</html>
```